Slide desk development general pellham stride

I am looking to expand the range of slide templates we have using our new branded powerpoint deck so the team have more options.

Target Market(s)

We operate in the construction sector

Industry/Entity Type

Construction

Requirements
Must have
• Picture linking back to construction

```html
<!DOCTYPE html>
<html lang="en">
<head>
<meta charset="utf-8">
<title>Pellham Stride – Slide Templates</title>
<link href="https://fonts.googleapis.com/css2?family=Inter:ital,wght@0,400;0,500;0,600;0,700;0,800;1,400&display=swap" rel="stylesheet">
<style>
  :root{
    --page:#ffffff;
    --slide:#000000;
    --panel:#101010;
    --green:#84d94f;
    --green-line:#6cc23c;
    --white:#ffffff;
    --text:#d9d9d9;
    --muted:#8a8a8a;
    --grey:#6e6e6e;
    --teal:#3f6f8c;
    --pink:#e0226e;
    --lime:#9acd32;
    --grid:#555555;
  }
  *{box-sizing:border-box;margin:0;padding:0}
  html,body{width:1033px;height:1200px;overflow:hidden;background:var(--page)}
  body{position:relative;font-family:"Inter",Arial,sans-serif;color:var(--white)}
  .slide{position:absolute;width:439px;height:246px;background:var(--slide);overflow:hidden}
  .s-cover{left:67px;top:62px}
  .s-process{left:534px;top:62px}
  .s-about{left:67px;top:331px}
  .s-collab{left:531px;top:331px}
  .s-solutions{left:67px;top:602px}
  .s-hex{left:531px;top:602px}
  .s-chart{left:64px;top:871px}
  .s-thanks{left:531px;top:877px}
  .abs{position:absolute}

  .brand{position:absolute;display:flex;align-items:center;gap:5px;font-family:"Inter",Arial,sans-serif;font-weight:600;color:var(--white);font-size:10px;letter-spacing:.1px;white-space:nowrap}
  .brand .mark{width:9px;height:9px;background:var(--green)}
  .slide-title{position:absolute;font-weight:700;font-size:13.5px;color:var(--white)}

  /* cover */
  .cover-photo{position:absolute;inset:0;background:linear-gradient(140deg,#2b3a4c 0%,#4d5f73 35%,#1e2836 70%,#0c1119 100%);clip-path:polygon(222px 0,439px 0,439px 246px,265px 246px)}
  .s-cover .brand{left:25px;top:38px;font-size:17px;gap:8px}
  .s-cover .brand .mark{width:14px;height:14px}
  .cover-title{position:absolute;left:27px;top:105px;font-size:20px;font-weight:800;color:var(--green);letter-spacing:-.2px}
  .cover-sub{position:absolute;left:28px;top:135px;width:190px;font-size:8.2px;line-height:15px;color:var(--text)}
  .cover-meta{position:absolute;left:28px;top:203px;font-size:8px;line-height:14px;color:var(--text)}

  /* process */
  .s-process .brand{left:18px;top:28px}
  .s-process .slide-title{left:117px;top:25px}
  .step{position:absolute;width:100px}
  .badge{position:absolute;width:17px;height:22px;background:var(--green);clip-path:polygon(0 0,100% 0,100% 70%,50% 100%,0 70%);font-size:7px;font-weight:700;color:#000;text-align:center;padding-top:3px}
  .step h3{position:absolute;font-size:8px;font-weight:500;color:var(--white)}
  .step p{position:absolute;font-size:4.2px;line-height:6.4px;color:var(--text);width:96px}

  /* about */
  .s-about .brand{left:10px;top:20px}
  .about-divider{position:absolute;left:101px;top:7px;width:1px;height:29px;background:var(--white)}
  .s-about .slide-title{left:115px;top:16px}
  .about-photo{position:absolute;left:13px;top:47px;width:216px;height:183px;background:linear-gradient(180deg,#8fa3b6 0%,#5c6f82 45%,#2a3440 80%,#3b2a2a 100%)}
  .about-copy{position:absolute;left:247px;top:54px;width:176px;font-size:5.3px;line-height:9.1px;color:var(--text)}
  .about-copy p+p{margin-top:9px}

  /* collaboration */
  .s-collab .brand{left:23px;top:24px}
  .collab-rule{position:absolute;left:26px;top:60px;width:1px;height:175px;background:var(--green-line)}
  .collab-title{position:absolute;left:65px;top:57px;font-size:17.5px;line-height:22px;color:var(--green);font-weight:500}
  .collab-title b{font-weight:700}
  .collab-item{position:absolute;left:26px;width:200px;height:20px}
  .collab-item::before{content:"";position:absolute;left:0;top:2px;width:23px;height:1px;background:var(--green-line)}
  .collab-item::after{content:"";position:absolute;left:30px;top:1px;width:3px;height:3px;border-radius:50%;background:var(--green)}
  .collab-item span{position:absolute;left:40px;top:-3px;width:160px;font-size:6px;line-height:10px;color:var(--text)}
  .collab-panel{position:absolute;left:254px;top:58px;width:164px;height:161px;background:var(--panel)}
  .collab-panel p{position:absolute;left:21px;top:38px;width:128px;font-style:italic;font-size:6.1px;line-height:10.3px;color:var(--teal)}

  /* solutions */
  .s-solutions .brand{left:19px;top:21px}
  .s-solutions .slide-title{left:111px;top:18px}
  .sol{position:absolute;width:120px}
  .sol svg{position:absolute;left:0;top:0;width:22px;height:22px}
  .sol h4{position:absolute;left:29px;top:2px;font-size:6.3px;line-height:8px;font-weight:700;color:var(--white)}
  .sol p{position:absolute;left:1px;top:30px;width:118px;font-size:5px;line-height:7.3px;color:var(--muted)}

  /* hexagons */
  .s-hex .brand{left:19px;top:21px}
  .s-hex .slide-title{left:112px;top:18px}
  .hex-art{position:absolute;left:0;top:0;width:439px;height:246px}
  .hex-label{position:absolute;width:70px;text-align:center;font-size:5.6px;line-height:8px;font-weight:600;color:#111}
  .hex-copy{position:absolute;width:84px;text-align:center;font-size:4.8px;line-height:7.3px;color:var(--muted)}

  /* chart */
  .s-chart .brand{left:19px;top:38px}
  .s-chart .slide-title{left:129px;top:17px}
  .chart-intro{position:absolute;left:129px;top:40px;width:292px;font-size:5.3px;line-height:8.2px;color:var(--text)}
  .chart{position:absolute;left:0;top:0;width:439px;height:246px}

  /* thanks */
  .thanks-photo{position:absolute;inset:0;background:radial-gradient(ellipse at 40% 60%,#262626 0%,#171717 55%,#0e0e0e 100%)}
  .s-thanks .brand{left:139px;top:56px;font-size:19px;gap:9px}
  .s-thanks .brand .mark{width:15px;height:15px}
  .thanks-rule{position:absolute;left:131px;width:177px;height:1px;background:var(--green-line)}
  .thanks-word{position:absolute;left:0;width:439px;top:133px;text-align:center;font-size:34px;font-weight:500;color:var(--white);letter-spacing:-.3px}
</style>
</head>
<body>

<!-- Cover -->
<section class="slide s-cover">
  <div class="cover-photo" role="img" aria-label="Construction site team reviewing project plans on a laptop"></div>
  <div class="brand"><span class="mark"></span>Pellham Stride</div>
  <h1 class="cover-title">Presentation Title</h1>
  <p class="cover-sub">Lorem Ipsum is simply dummy text of the printing and typesetting</p>
  <p class="cover-meta">12 Dec, 2025<br>Dana Whitfield</p>
</section>

<!-- Process -->
<section class="slide s-process">
  <div class="brand"><span class="mark"></span>Pellham Stride</div>
  <h2 class="slide-title">Our Process</h2>
  <svg class="abs" style="left:0;top:0" width="439" height="246" viewBox="0 0 439 246" aria-hidden="true">
    <path d="M17 64.5 H375 A44 44 0 0 1 375 152.5 H17" fill="none" stroke="#6cc23c" stroke-width="0.8"/>
  </svg>

  <div class="step" style="left:27px;top:65px"><div class="badge">01</div><h3 style="left:1px;top:29px">Discovery</h3><p style="left:2px;top:42px">Lorem ipsum dolor sit amet, consectetur adipiscing elit, sed do eiusmod tempor incididunt ut labore.</p></div>
  <div class="step" style="left:148px;top:65px"><div class="badge">02</div><h3 style="left:1px;top:29px">Design</h3><p style="left:2px;top:42px">Lorem ipsum dolor sit amet, consectetur adipiscing elit, sed do eiusmod tempor incididunt ut labore.</p></div>
  <div class="step" style="left:275px;top:65px"><div class="badge">03</div><h3 style="left:1px;top:29px">Development</h3><p style="left:2px;top:42px">Lorem ipsum dolor sit amet, consectetur adipiscing elit, sed do eiusmod tempor incididunt ut labore.</p></div>
  <div class="step" style="left:27px;top:153px"><div class="badge">04</div><h3 style="left:1px;top:27px">Retainer</h3><p style="left:2px;top:40px">Lorem ipsum dolor sit amet, consectetur adipiscing elit, sed do eiusmod tempor incididunt ut labore.</p></div>
  <div class="step" style="left:148px;top:153px"><div class="badge">05</div><h3 style="left:1px;top:27px">Launch</h3><p style="left:2px;top:40px">Lorem ipsum dolor sit amet, consectetur adipiscing elit, sed do eiusmod tempor incididunt ut labore.</p></div>
  <div class="step" style="left:275px;top:153px"><div class="badge">06</div><h3 style="left:1px;top:27px">QA</h3><p style="left:2px;top:40px">Lorem ipsum dolor sit amet, consectetur adipiscing elit, sed do eiusmod tempor incididunt ut labore.</p></div>
</section>

<!-- About -->
<section class="slide s-about">
  <div class="brand"><span class="mark"></span>Pellham Stride</div>
  <div class="about-divider"></div>
  <h2 class="slide-title">About Us</h2>
  <div class="about-photo" role="img" aria-label="Construction project team meeting around a table in a glass-walled site office"></div>
  <div class="about-copy">
    <p>Sed ut perspiciatis unde omnis iste natus error sit voluptatem accusantium doloremque laudantium, totam rem aperiam, eaque ipsa quae ab illo inventore veritatis et quasi architecto beatae vitae dicta sunt explicabo. Nemo enim ipsam voluptatem quia voluptas sit aspernatur aut odit aut fugit, sed quia consequuntur magni dolores eos qui ratione voluptatem sequi nesciunt. Neque porro quisquam est, qui dolorem ipsum quia dolor sit amet, consectetur, adipisci velit, sed quia non numquam eius modi tempora incidunt ut labore et dolore magnam aliquam quaerat voluptatem. Ut enim</p>
    <p>At vero eos et accusamus et iusto odio dignissimos ducimus qui blanditiis praesentium voluptatum deleniti atque corrupti quos dolores et quas molestias excepturi sint occaecati cupiditate non provident, similique sunt in culpa qui officia deserunt mollitia animi, id est laborum et dolorum fuga. Et harum quidem rerum facilis est</p>
  </div>
</section>

<!-- Collaboration -->
<section class="slide s-collab">
  <div class="brand"><span class="mark"></span>Pellham Stride</div>
  <div class="collab-rule"></div>
  <h2 class="collab-title">Collaboration<br><b>Opportunity</b></h2>
  <div class="collab-item" style="top:119px"><span>Sed ut perspiciatis unde omnis iste natus error sit voluptatem accusantium</span></div>
  <div class="collab-item" style="top:150px"><span>At vero eos et accusamus et iusto odio dignissimos ducimus qui blanditiis praesentium</span></div>
  <div class="collab-item" style="top:181px"><span>Nam libero tempore, cum soluta nobis est eligendi optio cumque nihil impedit quo minus</span></div>
  <div class="collab-item" style="top:212px"><span>Temporibus autem quibusdam et aut officiis debitis aut rerum necessitatibus saepe</span></div>
  <div class="collab-panel"><p>At vero eos et accusamus et iusto odio dignissimos ducimus qui blanditiis praesentium voluptatum deleniti atque corrupti quos dolores et quas molestias excepturi sint occaecati cupiditate non provident, similique sunt in culpa qui officia deserunt mollitia animi, id est laborum et dolorum</p></div>
</section>

<!-- Solutions -->
<section class="slide s-solutions">
  <div class="brand"><span class="mark"></span>Pellham Stride</div>
  <h2 class="slide-title">Solutions</h2>

  <div class="sol" style="left:21px;top:52px">
    <svg viewBox="0 0 24 24" fill="none" stroke="#84d94f" stroke-width="1.3" aria-hidden="true"><rect x="2" y="9" width="13" height="8"/><path d="M15 11h4l3 3v3h-7"/><circle cx="6" cy="19" r="2"/><circle cx="18" cy="19" r="2"/><path d="M4 9l3-5h6l2 5"/></svg>
    <h4>LOREM IPSUM DOLOR<br>SIT AMET</h4>
    <p>Sed ut perspiciatis unde omnis iste natus error sit voluptatem accusantium doloremque laudantium, totam rem aperiam, eaque ipsa quae ab illo inventore veritatis.</p>
  </div>
  <div class="sol" style="left:164px;top:52px">
    <svg viewBox="0 0 24 24" fill="none" stroke="#84d94f" stroke-width="1.3" aria-hidden="true"><rect x="3" y="4" width="13" height="17" rx="1"/><path d="M6 9h7M6 13h5M6 17h4"/><path d="M20 5l-7 9-1 3 3-1 7-9z"/></svg>
    <h4>LOREM IPSUM DOLOR<br>SIT AMET</h4>
    <p>Sed ut perspiciatis unde omnis iste natus error sit voluptatem accusantium doloremque laudantium, totam rem aperiam, eaque ipsa quae ab illo inventore veritatis.</p>
  </div>
  <div class="sol" style="left:306px;top:52px">
    <svg viewBox="0 0 24 24" fill="none" stroke="#84d94f" stroke-width="1.3" aria-hidden="true"><circle cx="12" cy="10" r="7"/><path d="M9 10l2 2 4-4"/><path d="M8 16l-2 6 6-3 6 3-2-6"/></svg>
    <h4>LOREM IPSUM DOLOR<br>SIT AMET</h4>
    <p>Sed ut perspiciatis unde omnis iste natus error sit voluptatem accusantium doloremque laudantium, totam rem aperiam, eaque ipsa quae ab illo inventore veritatis.</p>
  </div>
  <div class="sol" style="left:21px;top:149px">
    <svg viewBox="0 0 24 24" fill="none" stroke="#84d94f" stroke-width="1.3" aria-hidden="true"><rect x="5" y="3" width="15" height="18" rx="1"/><path d="M8 7h9M8 10h6"/><path d="M3 15l5-2 5 2-5 2z"/><path d="M5 16v3c2 1 4 1 6 0v-3"/></svg>
    <h4>LOREM IPSUM DOLOR<br>SIT AMET</h4>
    <p>Sed ut perspiciatis unde omnis iste natus error sit voluptatem accusantium doloremque laudantium, totam rem aperiam, eaque ipsa quae ab illo inventore veritatis.</p>
  </div>
  <div class="sol" style="left:164px;top:149px">
    <svg viewBox="0 0 24 24" fill="none" stroke="#84d94f" stroke-width="1.3" aria-hidden="true"><circle cx="13" cy="9" r="6"/><path d="M9 14l-6 7"/><path d="M3 21h18"/><path d="M17 14v7"/></svg>
    <h4>LOREM IPSUM DOLOR<br>SIT AMET</h4>
    <p>Sed ut perspiciatis unde omnis iste natus error sit voluptatem accusantium doloremque laudantium, totam rem aperiam, eaque ipsa quae ab illo inventore veritatis.</p>
  </div>
  <div class="sol" style="left:306px;top:149px">
    <svg viewBox="0 0 24 24" fill="none" stroke="#84d94f" stroke-width="1.3" aria-hidden="true"><circle cx="10" cy="10" r="3"/><path d="M10 2v3M10 15v3M2 10h3M15 10h3M4.3 4.3l2.1 2.1M13.6 13.6l2.1 2.1M4.3 15.7l2.1-2.1M13.6 6.4l2.1-2.1"/><path d="M15 17l5 5M19 15l3 3"/></svg>
    <h4>LOREM IPSUM DOLOR<br>SIT AMET</h4>
    <p>Sed ut perspiciatis unde omnis iste natus error sit voluptatem accusantium doloremque laudantium, totam rem aperiam, eaque ipsa quae ab illo inventore veritatis.</p>
  </div>
</section>

<!-- Hexagon feature -->
<section class="slide s-hex">
  <div class="brand"><span class="mark"></span>Pellham Stride</div>
  <h2 class="slide-title">Heading</h2>
  <svg class="hex-art" viewBox="0 0 439 246" aria-hidden="true">
    <defs>
      <linearGradient id="backing" x1="0" y1="0" x2="0" y2="1"><stop offset="0" stop-color="#8a8a8a"/><stop offset="1" stop-color="#4a4a4a"/></linearGradient>
    </defs>
    <g fill="url(#backing)" stroke="url(#backing)" stroke-width="10" stroke-linejoin="round">
      <polygon points="70,62 117,89 117,130 70,157 14,130 14,89"/>
      <polygon points="167,110 214,83 214,138 167,178 120,138 120,83"/>
      <polygon points="268,62 315,89 315,130 268,157 221,130 221,89"/>
      <polygon points="368,110 415,83 415,138 368,178 321,138 321,83"/>
    </g>
    <g fill="#fafafa" stroke="#fafafa" stroke-width="9" stroke-linejoin="round">
      <polygon points="70,85 107,106 107,149 70,170 33,149 33,106"/>
      <polygon points="167,85 204,106 204,149 167,170 130,149 130,106"/>
      <polygon points="268,85 305,106 305,149 268,170 231,149 231,106"/>
      <polygon points="368,85 405,106 405,149 368,170 331,149 331,106"/>
    </g>
    <g fill="none" stroke="#84d94f" stroke-width="1" stroke-linejoin="round">
      <path d="M70 113l9 5-9 5-9-5z M61 118v9l9 5 9-5v-9 M70 123v9"/>
      <path d="M174 112c-6 1-11 6-13 13l4 4c7-2 12-7 13-13z M163 123l-4 1-2 4 4-1 M170 129l-1 4-4 2 1-4 M161 129l-3 3"/>
      <circle cx="268" cy="121" r="8"/><path d="M260 121h16 M268 113c-4 4-4 12 0 16 M268 113c4 4 4 12 0 16"/>
      <path d="M361 113h6v3a2 2 0 0 0 4 0v-3h6v6h-3a2 2 0 0 0 0 4h3v7h-16z"/>
    </g>
  </svg>
  <div class="hex-label" style="left:35px;top:135px">LOREM IPSUM<br>DOLOR</div>
  <div class="hex-label" style="left:132px;top:135px">LOREM IPSUM<br>DOLOR</div>
  <div class="hex-label" style="left:233px;top:135px">LOREM IPSUM<br>DOLOR</div>
  <div class="hex-label" style="left:333px;top:135px">LOREM IPSUM<br>DOLOR</div>
  <p class="hex-copy" style="left:28px;top:173px">Sed ut perspiciatis unde omnis iste natus error sit voluptatem accusantium doloremque laudantium.</p>
  <p class="hex-copy" style="left:125px;top:187px">Sed ut perspiciatis unde omnis iste natus error sit voluptatem accusantium doloremque laudantium.</p>
  <p class="hex-copy" style="left:226px;top:173px">Sed ut perspiciatis unde omnis iste natus error sit voluptatem accusantium doloremque laudantium.</p>
  <p class="hex-copy" style="left:326px;top:187px">Sed ut perspiciatis unde omnis iste natus error sit voluptatem accusantium doloremque laudantium.</p>
</section>

<!-- Chart -->
<section class="slide s-chart">
  <div class="brand"><span class="mark"></span>Pellham Stride</div>
  <h2 class="slide-title">Heading</h2>
  <p class="chart-intro">Lorem ipsum dolor sit amet, consectetur adipiscing elit, sed do eiusmod tempor incididunt ut labore et dolore magna aliqua. Ut enim ad minim veniam, quis nostrud exercitation ullamco laboris nisi ut aliquip ex ea commodo consequat. Duis aute irure dolor in reprehenderit in voluptate velit.</p>
  <svg class="chart" viewBox="0 0 439 246" role="img" aria-label="Line chart of monthly sales and orders">
    <g font-family="Inter, Arial, sans-serif" font-size="4" fill="#666">
      <circle cx="369" cy="80" r="2.4" fill="#e0226e"/><text x="373" y="81.5">Sales</text>
      <circle cx="401" cy="80" r="2.4" fill="#9acd32"/><text x="405" y="81.5">Orders</text>
    </g>
    <g stroke="#555" stroke-width="0.5">
      <path d="M26 87H421M26 100.4H421M26 113.8H421M26 127.2H421M26 140.6H421M26 154H421M26 167.4H421M26 180.8H421M26 194.2H421M26 207.6H421M26 221H421"/>
      <path d="M26 87V221M58.9 87V221M91.8 87V221M124.7 87V221M157.6 87V221M190.5 87V221M223.4 87V221M256.3 87V221M289.2 87V221M322.1 87V221M355 87V221M387.9 87V221M420.8 87V221"/>
    </g>
    <g font-family="Inter, Arial, sans-serif" font-size="3.6" fill="#666" text-anchor="end">
      <text x="23" y="88">100</text><text x="23" y="101.5">90</text><text x="23" y="115">80</text><text x="23" y="128.5">70</text><text x="23" y="142">60</text><text x="23" y="155">50</text><text x="23" y="168.5">40</text><text x="23" y="182">30</text><text x="23" y="195.5">20</text><text x="23" y="209">10</text><text x="23" y="222">0</text>
    </g>
    <g font-family="Inter, Arial, sans-serif" font-size="3.6" fill="#666" text-anchor="middle">
      <text x="42" y="231">JAN</text><text x="75" y="231">FEB</text><text x="108" y="231">MAR</text><text x="141" y="231">APR</text><text x="174" y="231">MAY</text><text x="207" y="231">JUN</text><text x="240" y="231">JUL</text><text x="273" y="231">AUG</text><text x="306" y="231">SEP</text><text x="338" y="231">OCT</text><text x="371" y="231">NOV</text><text x="404" y="231">DEC</text>
    </g>
    <polyline fill="none" stroke="#9acd32" stroke-width="0.8" points="26,167.4 58.9,154 91.8,167.4 124.7,127.2 157.6,127.2 190.5,140.6 223.4,127.2 256.3,127.2 289.2,105.8 322.1,100.4 355,100.4 387.9,105.8 420.8,100.4"/>
    <polyline fill="none" stroke="#e0226e" stroke-width="0.8" points="26,207.6 58.9,180.8 91.8,194.2 124.7,154 157.6,140.6 190.5,167.4 223.4,154 256.3,167.4 322.1,113.8 387.9,140.6 420.8,113.8"/>
    <g fill="#9acd32">
      <circle cx="26" cy="167.4" r="1.5"/><circle cx="58.9" cy="154" r="1.5"/><circle cx="91.8" cy="167.4" r="1.5"/><circle cx="124.7" cy="127.2" r="1.5"/><circle cx="157.6" cy="127.2" r="1.5"/><circle cx="190.5" cy="140.6" r="1.5"/><circle cx="223.4" cy="127.2" r="1.5"/><circle cx="256.3" cy="127.2" r="1.5"/><circle cx="289.2" cy="105.8" r="1.5"/><circle cx="322.1" cy="100.4" r="1.5"/><circle cx="355" cy="100.4" r="1.5"/><circle cx="387.9" cy="105.8" r="1.5"/><circle cx="420.8" cy="100.4" r="1.5"/>
    </g>
    <g fill="#e0226e">
      <circle cx="26" cy="207.6" r="1.5"/><circle cx="58.9" cy="180.8" r="1.5"/><circle cx="91.8" cy="194.2" r="1.5"/><circle cx="124.7" cy="154" r="1.5"/><circle cx="157.6" cy="140.6" r="1.5"/><circle cx="190.5" cy="167.4" r="1.5"/><circle cx="223.4" cy="154" r="1.5"/><circle cx="256.3" cy="167.4" r="1.5"/><circle cx="322.1" cy="113.8" r="1.5"/><circle cx="387.9" cy="140.6" r="1.5"/><circle cx="420.8" cy="113.8" r="1.5"/>
    </g>
  </svg>
</section>

<!-- Closing -->
<section class="slide s-thanks">
  <div class="thanks-photo" role="img" aria-label="Darkened photo of a construction team meeting in a site office"></div>
  <div class="brand"><span class="mark"></span>Pellham Stride</div>
  <div class="thanks-rule" style="top:128px"></div>
  <div class="thanks-word">Thank You</div>
  <div class="thanks-rule" style="top:187px"></div>
</section>

</body>
</html>
```